Email Signatures

I would like to create a new email signature for my team. The design will be the same for everyone, with only individual details such as name and email changing. You can also see our brand style on our website. https://www.tlmbespokehomes.com.au/

Target Market(s)

Clients for new builds or renovations

Industry/Entity Type

Construction

Colors

Designer to choose colors to be used in the design.

```html
<!DOCTYPE html>
<html lang="en">
<head>
<meta charset="utf-8">
<title>TLM Bespoke Homes – Email Signature</title>
<link href="https://fonts.googleapis.com/css2?family=Barlow:wght@400;500;700&display=swap" rel="stylesheet">
<style>
  :root {
    --page-bg: #e4e4e4;
    --sig-bg: #000000;
    --brand-green: #0a9a48;
    --text-white: #ffffff;
  }
  * { margin: 0; padding: 0; box-sizing: border-box; }
  html, body {
    width: 1200px; height: 1000px; overflow: hidden;
    background: var(--page-bg);
    font-family: "Barlow", Arial, sans-serif;
  }
  .signature {
    position: absolute; left: 87px; top: 321px;
    width: 1026px; height: 357px;
    background: var(--sig-bg);
    overflow: hidden;
  }
  .signature__band {
    position: absolute; left: 0; right: 0; bottom: 0; height: 20px;
    background: linear-gradient(to bottom, #000 0%, var(--brand-green) 90%);
  }
  .brand {
    position: absolute; left: 70px; top: 145px; width: 340px;
    display: flex; align-items: center; justify-content: center; gap: 14px;
  }
  .brand__mark { width: 18px; height: 18px; background: var(--brand-green); flex: none; }
  .brand__name {
    color: var(--text-white); font-weight: 700; font-size: 30px;
    letter-spacing: 3px; white-space: nowrap;
  }
  .divider {
    position: absolute; left: 469px; top: 55px; width: 2px; height: 246px;
    background: var(--brand-green);
  }
  .person { position: absolute; left: 550px; top: 52px; color: var(--text-white); }
  .person__name { font-weight: 700; font-size: 44px; letter-spacing: 1.5px; line-height: 1; }
  .person__role { font-weight: 500; font-size: 22px; letter-spacing: 2px; margin-top: 10px; }
  .contacts { position: absolute; left: 550px; top: 174px; list-style: none; }
  .contacts__item {
    display: flex; align-items: center; gap: 12px; height: 31px;
    color: var(--text-white); font-size: 20px;
  }
  .contacts__icon { width: 24px; height: 24px; fill: var(--brand-green); flex: none; }
</style>
</head>
<body>
  <section class="signature" aria-label="Email signature">
    <div class="brand">
      <span class="brand__mark"></span>
      <span class="brand__name">TLM BESPOKE HOMES</span>
    </div>
    <div class="divider"></div>
    <div class="person">
      <h1 class="person__name">LIAM CARTER</h1>
      <p class="person__role">GENERAL MANAGER</p>
    </div>
    <ul class="contacts">
      <li class="contacts__item">
        <svg class="contacts__icon" viewBox="0 0 24 24" aria-hidden="true"><path d="M6.6 10.8a15 15 0 0 0 6.6 6.6l2.2-2.2c.3-.3.7-.4 1-.2 1.1.4 2.3.6 3.6.6.6 0 1 .4 1 1V20c0 .6-.4 1-1 1A17 17 0 0 1 3 4c0-.6.4-1 1-1h3.5c.6 0 1 .4 1 1 0 1.3.2 2.5.6 3.6.1.3 0 .7-.2 1z"/></svg>
        <span>0400 123 456</span>
      </li>
      <li class="contacts__item">
        <svg class="contacts__icon" viewBox="0 0 24 24" aria-hidden="true"><path d="M2 5h20v14H2z M3.5 6.5 12 13l8.5-6.5" stroke="#000" stroke-width="1.5"/></svg>
        <span>info@tlmbespokehomes.com.au</span>
      </li>
      <li class="contacts__item">
        <svg class="contacts__icon" viewBox="0 0 24 24" aria-hidden="true"><circle cx="12" cy="12" r="10"/><path d="M2 12h20M12 2v20M5 6.5h14M5 17.5h14M12 2c-5 5-5 15 0 20M12 2c5 5 5 15 0 20" fill="none" stroke="#000" stroke-width="1.2"/></svg>
        <span>tlmbespokehomes.com.au</span>
      </li>
      <li class="contacts__item">
        <svg class="contacts__icon" viewBox="0 0 24 24" aria-hidden="true"><path d="M12 2a7 7 0 0 0-7 7c0 5 7 13 7 13s7-8 7-13a7 7 0 0 0-7-7zm0 9.5A2.5 2.5 0 1 1 12 6.5a2.5 2.5 0 0 1 0 5z"/></svg>
        <span>Devonport, Tasmania, Australia</span>
      </li>
    </ul>
    <div class="signature__band"></div>
  </section>
</body>
</html>
```